Webdesign project for healthcare IT company

Home, About, Solution, Contact, and Employment pages.

Please match the designs uploaded for colors and effect.

Please choose appropriate healthcare IT related photos to the content. Be sure to include the content that i've attached in the word document.

Please use the following URLs as reference:

www.veltrocare.example
www.dusk.example
www.plainagree.example

Target Market(s)

healthcare providers, doctors, nurses, c-level executives

Industry/Entity Type

Healthcare

Coding

Coded - Design and coding required

Number of Pages Required

5+ page

Font styles to use
Serif
Sans Serif

Colors
6b449b
0455a3
ffffff
333333
959595

Requirements
Must have
• B2B feel, matches the colors in the uploaded design files, images that can be purchased later that meet the content that I've uploaded

```html
<!DOCTYPE html>
<html lang="en">
<head>
<meta charset="utf-8">
<title>Norvane Technologies</title>
<link rel="stylesheet" href="https://fonts.googleapis.com/css2?family=Poppins:wght@300;400;500;600&display=swap">
<style>
:root{
  --blue:#0d4aa0;
  --blue-deep:#0455a3;
  --violet:#6b449b;
  --ink:#333333;
  --muted:#959595;
  --white:#ffffff;
  --panel:#f3f3f3;
  --footer:#262626;
  --rule:#8e86c6;
}
*{box-sizing:border-box;margin:0;padding:0}
html,body{width:1200px;height:2736px;overflow:hidden}
body{position:relative;font-family:"Poppins",sans-serif;color:var(--ink);background:var(--white)}
.abs{position:absolute}

/* header */
.site-header{left:0;top:0;width:1200px;height:100px;background:var(--white)}
.brand{left:86px;top:14px;display:flex;align-items:center;gap:12px}
.brand-mark{width:22px;height:22px;background:var(--violet)}
.brand-name{font-family:"Poppins",sans-serif;font-weight:500;color:var(--violet);font-size:24px;line-height:26px;letter-spacing:3px;text-transform:uppercase}
.brand-name small{display:block;font-size:24px;letter-spacing:3px}
.topbar{right:90px;top:13px;display:flex;gap:44px;font-size:13px;color:var(--ink)}
.topbar span{display:flex;align-items:center;gap:12px}
.topbar svg{width:16px;height:16px}
.topbar .phone{font-weight:600}
.topbar-rule{left:648px;top:48px;width:462px;height:1px;background:#e2e2e2}
.main-nav{right:90px;top:64px;display:flex;font-size:14px}
.main-nav a{color:var(--ink);text-decoration:none;padding:0 33px;border-left:1px solid #cfcfcf;line-height:22px}
.main-nav a:first-child{border-left:none}
.main-nav a:last-child{padding-right:0}

/* hero */
.hero{left:0;top:100px;width:1200px;height:699px;background:linear-gradient(100deg,#2b3644 0%,#4f6275 35%,#8fa2b4 60%,#3c4a5a 100%)}
.hero-title{left:86px;top:290px;color:var(--white);font-weight:300;font-size:56px;line-height:1.5}
.hero-title .big{display:block;font-size:60px;font-weight:400}
.btn{display:flex;align-items:center;justify-content:center;background:var(--blue);color:var(--white);font-size:24px;border-radius:40px;text-decoration:none}
.hero-btn{left:86px;top:586px;width:230px;height:69px}

/* about */
.about{left:0;top:799px;width:1200px;height:542px;background:var(--panel)}
.about-title{left:86px;top:866px;font-size:41px;font-weight:400}
.about-rule{left:86px;top:932px;width:120px;height:2px;background:var(--rule)}
.about-lead{left:86px;top:974px;font-size:18px;line-height:32px}
.about-body{left:86px;top:1056px;width:520px;font-size:13.5px;line-height:25.5px;color:#555}
.about-btn{left:86px;top:1206px;width:190px;height:58px;font-size:20px}

/* contact card */
.contact-card{left:662px;top:726px;width:450px;height:545px;background:var(--white);box-shadow:0 2px 8px rgba(0,0,0,.15)}
.contact-card h2{height:77px;background:var(--blue);color:var(--white);font-weight:400;font-size:31px;display:flex;align-items:center;justify-content:center}
.field{position:absolute;left:44px;width:356px;border-bottom:1px solid #555;font-size:11px;padding-bottom:4px}
.submit{position:absolute;left:155px;top:445px;width:151px;height:46px;background:var(--blue);color:var(--white);font-size:20px;display:flex;align-items:center;justify-content:center}

/* emergency */
.emergency-photo{left:0;top:1363px;width:587px;height:244px;background:linear-gradient(90deg,#5f8f6a 0%,#c79f86 30%,#e7cbb6 55%,#dfe6ee 100%)}
.emergency{left:609px;top:1363px;width:591px;height:244px;background:var(--blue-deep)}
.emergency-kicker{left:693px;top:1395px;font-size:32px;color:#7fb0ee;font-weight:300}
.emergency-call{left:693px;top:1444px;font-size:37px;color:var(--white)}
.emergency-rule{left:857px;top:1478px;width:243px;height:1px;background:#5d8fd0}
.emergency-phone{left:693px;top:1515px;display:flex;align-items:center;gap:16px;font-size:37px;color:var(--white);font-weight:300}
.emergency-phone svg{width:48px;height:48px}

/* work */
.work-title{left:0;top:1664px;width:1200px;text-align:center;font-size:42px;font-weight:400}
.work-rule{top:1700px;width:120px;height:2px;background:var(--rule)}
.card-photo{top:1778px;width:324px;height:270px}
.card{top:2068px;width:324px;height:219px;background:var(--panel);text-align:center;padding:0 26px}
.card h3{margin-top:36px;font-size:25px;font-weight:400}
.card hr{width:40px;margin:10px auto 14px;border:none;border-top:1px solid #888}
.card p{font-size:13.5px;line-height:24px;color:#555}

/* footer */
.site-footer{left:0;top:2347px;width:1200px;height:389px;background:var(--footer)}
.footer-map{left:86px;top:2420px;width:609px;height:243px;background:linear-gradient(135deg,#e6e4dd 0%,#d9dcd6 45%,#9fc3e6 55%,#e3e1da 70%)}
.footer-brand{left:762px;top:2452px;display:flex;align-items:center;gap:14px}
.footer-brand .brand-mark{width:26px;height:26px;background:var(--white)}
.footer-brand .brand-name{color:var(--white);font-size:30px;line-height:34px}
.footer-brand .brand-name small{font-size:30px}
.social{left:766px;top:2588px;display:flex;align-items:center;gap:18px;color:var(--white);font-size:30px}
.social i{display:block;width:26px;height:26px;border-radius:50%;background:#2f83d8}
.social i:first-of-type{margin-left:6px}
.copyright{left:766px;top:2652px;font-size:12px;color:#bdbdbd}
</style>
</head>
<body>

<header class="site-header abs">
  <div class="brand abs">
    <span class="brand-mark"></span>
    <span class="brand-name">Norvane<small>Technologies</small></span>
  </div>
  <div class="topbar abs">
    <span><svg viewBox="0 0 16 16"><circle cx="8" cy="8" r="8" fill="#0d4aa0"/><rect x="4" y="5" width="8" height="6" fill="none" stroke="#fff" stroke-width="1.2"/><path d="M4 5l4 3 4-3" fill="none" stroke="#fff" stroke-width="1.2"/></svg>info@norvanetech.example</span>
    <span class="phone"><svg viewBox="0 0 16 16"><circle cx="8" cy="8" r="8" fill="#0d4aa0"/><rect x="5.5" y="3.5" width="5" height="9" rx="1" fill="none" stroke="#fff" stroke-width="1.2"/></svg>1-888-555-0142</span>
  </div>
  <div class="topbar-rule abs"></div>
  <nav class="main-nav abs">
    <a href="#">Home</a><a href="#">About</a><a href="#">Solutiont</a><a href="#">Employment</a><a href="#">Contact</a>
  </nav>
</header>

<section class="hero abs" role="img" aria-label="Close-up photo of a hand holding a computer chip over a circuit board"></section>
<h1 class="hero-title abs">Creating a Healthier<span class="big">TODAY</span>Tomorrow</h1>
<a class="btn hero-btn abs" href="#">Learn More</a>

<section class="about abs"></section>
<h2 class="about-title abs">What we do</h2>
<div class="about-rule abs"></div>
<p class="about-lead abs">There are many variations of ,<br>but the majority have suffered alteration in some form</p>
<p class="about-body abs">To make saving you money as easy as possible, mysavings.example has been conveniently positioned into 5 categories. Each category contains separate and unique benefits which enable our members to save literally thousands of dollars every year! Membership.</p>
<a class="btn about-btn abs" href="#">Learn More</a>

<form class="contact-card abs">
  <h2>Contact Us</h2>
  <div class="field" style="top:135px">Name*</div>
  <div class="field" style="top:198px">Email*</div>
  <div class="field" style="top:262px">Phone*</div>
  <div class="field" style="top:367px">Address*</div>
  <div class="submit">Submit</div>
</form>

<div class="emergency-photo abs" role="img" aria-label="Photo of two people holding hands in a caring gesture"></div>
<section class="emergency abs"></section>
<p class="emergency-kicker abs">Need an Emergency Help?</p>
<p class="emergency-call abs">Call Us!</p>
<div class="emergency-rule abs"></div>
<p class="emergency-phone abs"><svg viewBox="0 0 48 48"><circle cx="24" cy="24" r="21" fill="none" stroke="#7fb0ee" stroke-width="2.5"/><path d="M17 13c2 0 3 5 3 6s-2 2-2 3 4 7 7 8c1 0 2-2 3-2s6 1 6 3-2 4-4 4c-8 0-17-10-17-18 0-2 2-4 4-4z" fill="#7fb0ee"/></svg>1 800 555 01 76</p>

<h2 class="work-title abs">Our Work</h2>
<div class="work-rule abs" style="left:361px"></div>
<div class="work-rule abs" style="left:715px"></div>

<div class="card-photo abs" style="left:86px;background:linear-gradient(135deg,#2b2622,#8a7a5e 50%,#d7ceb4)" role="img" aria-label="Photo of an old beige desktop computer"></div>
<div class="card-photo abs" style="left:436px;background:linear-gradient(135deg,#6e5038,#3a7f99 50%,#b58a4d)" role="img" aria-label="Photo of a tablet showing a padlock among repair tools"></div>
<div class="card-photo abs" style="left:786px;background:linear-gradient(135deg,#bcc6cc,#8e9aa2 50%,#d8dde0)" role="img" aria-label="Photo of two engineers assembling a 3D printer"></div>

<article class="card abs" style="left:86px"><h3>Computer Archeology</h3><hr><p>Need data off a legacy system that you would like to sunset? We can help you with that.</p></article>
<article class="card abs" style="left:436px"><h3>Digital Check In</h3><hr><p>Still using clipboards to check people into your facility? Struggling to get that paper-based information into your system? We can help you with that.</p></article>
<article class="card abs" style="left:786px"><h3>Norvane3D</h3><hr><p>Have something in mind that you need printed, but don't have a 3D printer? We can help you design it, and print it for you.</p></article>

<footer class="site-footer abs"></footer>
<div class="footer-map abs" role="img" aria-label="Street map of the office location beside a river"></div>
<div class="footer-brand abs">
  <span class="brand-mark"></span>
  <span class="brand-name">Norvane<small>Technologies</small></span>
</div>
<div class="social abs">Social Links <i></i><i></i><i></i><i></i></div>
<p class="copyright abs">© 2017 norvane. Copy Right Reserved.</p>

</body>
</html>
```